Miss Dorrel Teen Postcard for special events

Need creative display for platform of logo for Miss Dorrel on her large postcards. Be kind, be bold, be brave, be you is the message. Please include this quote:
Kindness is the language which the deaf can hear
and the blind can see. - Hobart Lune
Her title is 2017 Miss Dorrel Hollin Starlet Teen. Her name is Corinne Vask. We have pics that we want included on the card. We want it to have a front and back. You can use any combination of the photos. thanks!

Target Market(s)

Youth/ Young Adults

Industry/Entity Type

Events

Font styles to use
Sans Serif
Script

Colors
86cfc6
33b8a4
3276b5
0255a3

Requirements
Must have
• Kindness is the language which the deaf can hear
• and the blind can see. - Hobart Lune
• Title-
• Name
• She is partial to the jumpsuit photo for the front but open to others
• Be Kind, Be Bold, Be Brave, Be you - would like this on the front
• Also please include Instgram: crvask202 twitter: crvask202 corinne47@pelvomail.net
• #kindboldbrave
Nice to have
• Anything that would inspire youth especially. Have begun events at hospitals and lining up work to assist with donations for community resources but not sure that is appropriate for this. We lean more towards the green than the blue, unless it ties with other things you see better- or a better shade.thanks
Should not have
• Should be age appropriate and appropriate for all ages.
• Postcard is for handing out / does not need to be mailed. Can seek revisions if this becomes the case

```html
<!DOCTYPE html>
<html lang="en">
<head>
<meta charset="utf-8">
<title>Miss Dorrel Teen – Event Postcard</title>
<link href="https://fonts.googleapis.com/css2?family=Montserrat:wght@500;600;700&family=Poppins:wght@200&family=Great+Vibes&family=Roboto+Condensed:wght@400&family=Open+Sans:ital,wght@1,400&display=swap" rel="stylesheet">
<style>
  :root {
    --page-bg: #e9ebec;
    --mint: #86cfc6;
    --mint-pale: #d8f1ee;
    --teal: #33b8a4;
    --blue: #3276b5;
    --navy: #0255a3;
    --ink: #1f2a33;
    --ink-navy: #1d4c86;
    --gold: #d2b04c;
    --white: #ffffff;
  }
  html, body {
    margin: 0;
    width: 1200px;
    height: 1047px;
    overflow: hidden;
    background: var(--page-bg);
  }
  .postcard {
    position: absolute;
    left: 268px;
    width: 663px;
    height: 480px;
    box-shadow: 0 4px 10px rgba(0,0,0,0.25);
  }
  .postcard--front { top: 34px; }
  .postcard--back { top: 537px; }
  .postcard svg { display: block; width: 100%; height: 100%; }

  .sans { font-family: "Montserrat", sans-serif; }
  .year { font-family: "Poppins", sans-serif; font-weight: 200; }
  .script { font-family: "Great Vibes", cursive; }
  .italic { font-family: "Open Sans", sans-serif; font-style: italic; }
  .condensed { font-family: "Roboto Condensed", sans-serif; }
</style>
</head>
<body>

<section class="postcard postcard--front" aria-label="Postcard front">
  <svg viewBox="0 0 829 600" xmlns="http://www.w3.org/2000/svg">
    <defs>
      <linearGradient id="photoTone" x1="0" y1="0" x2="1" y2="1">
        <stop offset="0" stop-color="#9bb28c"/>
        <stop offset="0.45" stop-color="#c9b8a8"/>
        <stop offset="1" stop-color="#b46f55"/>
      </linearGradient>
      <linearGradient id="panelTone" x1="0" y1="0" x2="1" y2="1">
        <stop offset="0" stop-color="#c6ece6"/>
        <stop offset="0.6" stop-color="var(--mint-pale)"/>
        <stop offset="1" stop-color="#f3fbfa"/>
      </linearGradient>
      <linearGradient id="badgeTone" x1="0" y1="0" x2="0" y2="1">
        <stop offset="0" stop-color="var(--teal)"/>
        <stop offset="1" stop-color="var(--blue)"/>
      </linearGradient>
    </defs>

    <rect class="hero-photo" x="0" y="0" width="829" height="600" fill="url(#photoTone)" role="img" aria-label="Photo of Corinne Vask in a rust jumpsuit on a city street"/>

    <path class="info-panel" d="M640,0 C545,35 482,140 487,260 L490,400 A86,86 0 0 1 400,570 Q370,595 335,600 L829,600 L829,0 Z" fill="url(#panelTone)"/>
    <path class="gold-edge" d="M640,0 C545,35 482,140 487,260 L490,400 A86,86 0 0 1 400,570 Q370,595 335,600" fill="none" stroke="var(--gold)" stroke-width="8"/>

    <g class="hashtag-badge">
      <circle cx="462" cy="486" r="85" fill="url(#badgeTone)" stroke="var(--gold)" stroke-width="6"/>
      <text class="condensed" x="462" y="494" font-size="23" fill="var(--white)" text-anchor="middle">#kindboldbrave</text>
    </g>

    <text class="sans brand" x="683" y="63" font-size="24" font-weight="700" fill="var(--ink)" text-anchor="middle">Miss Dorrel</text>
    <text class="year" x="683" y="170" font-size="84" fill="var(--ink)" text-anchor="middle">2017</text>
    <text class="sans title" x="684" y="212" font-size="33" font-weight="500" fill="var(--ink)" text-anchor="middle">Miss Dorrel</text>
    <text class="sans subtitle" x="684" y="236" font-size="18" font-weight="500" fill="var(--ink)" text-anchor="middle">Hollin Starlet Teen</text>

    <g class="motto" fill="var(--ink)">
      <text class="script" x="510" y="326" font-size="42">Be Kind</text>
      <text class="italic" x="586" y="358" font-size="25">Be Bold</text>
      <text class="script" x="638" y="402" font-size="42">Be Brave</text>
      <text class="italic" x="713" y="433" font-size="25">Be you</text>
    </g>

    <g class="contacts sans" font-size="16" fill="#333" font-weight="500">
      <circle cx="597" cy="476" r="8" fill="var(--teal)"/>
      <text x="625" y="482">crvask202</text>
      <circle cx="597" cy="516" r="8" fill="var(--teal)"/>
      <text x="625" y="522">crvask202</text>
      <circle cx="597" cy="558" r="8" fill="var(--teal)"/>
      <text x="625" y="564" font-size="15.5">corinne47@pelvomail.net</text>
    </g>
  </svg>
</section>

<section class="postcard postcard--back" aria-label="Postcard back">
  <svg viewBox="0 0 829 600" xmlns="http://www.w3.org/2000/svg">
    <defs>
      <linearGradient id="backTone" x1="0" y1="0" x2="0.3" y2="1">
        <stop offset="0" stop-color="#93d3cd"/>
        <stop offset="0.5" stop-color="#cfe6e8"/>
        <stop offset="1" stop-color="#dfe9ef"/>
      </linearGradient>
      <linearGradient id="boxTone" x1="0" y1="0" x2="0" y2="1">
        <stop offset="0" stop-color="var(--teal)"/>
        <stop offset="1" stop-color="var(--blue)"/>
      </linearGradient>
      <linearGradient id="portraitTone" x1="0" y1="0" x2="1" y2="1">
        <stop offset="0" stop-color="#7a5a44"/>
        <stop offset="1" stop-color="#d8b39a"/>
      </linearGradient>
      <linearGradient id="portraitToneGold" x1="0" y1="0" x2="1" y2="1">
        <stop offset="0" stop-color="#f2b937"/>
        <stop offset="1" stop-color="#c98f52"/>
      </linearGradient>
    </defs>

    <rect class="back-bg" x="0" y="0" width="829" height="600" fill="url(#backTone)"/>

    <g class="portrait-strip" stroke="var(--blue)" stroke-width="4">
      <rect x="30" y="31" width="166" height="166" fill="url(#portraitTone)" role="img" aria-label="Close-up portrait of Corinne Vask"/>
      <rect x="30" y="215" width="166" height="166" fill="url(#portraitTone)" role="img" aria-label="Smiling portrait of Corinne Vask with hand in hair"/>
      <rect x="30" y="403" width="166" height="166" fill="url(#portraitToneGold)" role="img" aria-label="Portrait of Corinne Vask against a yellow backdrop"/>
    </g>

    <g class="quote-box">
      <rect x="229" y="31" width="571" height="144" fill="url(#boxTone)" stroke="var(--gold)" stroke-width="6"/>
      <g class="sans" fill="var(--white)" font-weight="600" font-size="21">
        <text x="244" y="70" font-size="26">“</text>
        <text x="275" y="77">Kindness is the language which the deaf</text>
        <text x="280" y="121">can hear  and the blind can see.</text>
        <text x="672" y="112" font-size="26">”</text>
        <text x="784" y="150" text-anchor="end" font-size="22">- Hobart Lune</text>
      </g>
    </g>

    <g class="fill-lines sans" fill="var(--ink-navy)">
      <text x="245" y="254" font-size="28" font-weight="600">Title</text>
      <line x1="334" y1="252" x2="786" y2="252" stroke="var(--ink-navy)" stroke-width="3" stroke-dasharray="2 4"/>
      <text x="245" y="323" font-size="28" font-weight="600">Name</text>
      <line x1="355" y1="321" x2="783" y2="321" stroke="var(--ink-navy)" stroke-width="3" stroke-dasharray="2 4"/>
    </g>

    <g class="hashtag-box">
      <rect x="364" y="383" width="325" height="100" fill="url(#boxTone)" stroke="var(--gold)" stroke-width="6"/>
      <text class="condensed" x="526" y="449" font-size="44" fill="var(--white)" text-anchor="middle">#kindboldbrave</text>
    </g>

    <g class="contacts sans" fill="var(--ink-navy)" font-weight="700" font-size="17">
      <circle cx="257" cy="561" r="8" fill="var(--ink-navy)"/>
      <text x="285" y="567">crvask202</text>
      <circle cx="421" cy="561" r="8" fill="var(--ink-navy)"/>
      <text x="449" y="567">crvask202</text>
      <circle cx="577" cy="561" r="8" fill="var(--ink-navy)"/>
      <text x="597" y="567" font-size="15.5">corinne47@pelvomail.net</text>
    </g>
  </svg>
</section>

</body>
</html>
```